依頼詳細
ゴミ屋敷の片づけ・遺品整理等の事業になります。
ポスティングを想定しています。
ターゲットは高齢者になりますのでわかりやすいデザインでお願いします。
記載項目
屋号:そよかぜクリーンサービス
電話番号:未定
サイズ
A4
ページ数
両面
希望イメージ
シンプル 複雑
単色 カラフル
暗い 明るい
日常 高級
遊び心 厳粛
未来的 伝統的
女性的 男性的
希望する色
緑系
納品ファイル
• 高解像度JPG (.jpg)
補足説明
■ 選んだ理由

高齢者向けということでイラストを多用しわかりやすいデザインで気に入りました。
ベースもやさしめの色合いで好きです。

■ 提案者全員のお礼・コメント

さまざまな提案をいただき感謝しています。ありがとうございました。

```html
<!DOCTYPE html>
<html lang="ja">
<head>
<meta charset="utf-8">
<title>そよかぜクリーンサービス</title>
<link href="https://fonts.googleapis.com/css2?family=M+PLUS+Rounded+1c:wght@400;700;800;900&display=swap" rel="stylesheet">
<style>
:root{
  --green:#74b83a;
  --green-dark:#4f9a22;
  --green-pale:#eaf4da;
  --green-soft:#d6ebb8;
  --blue:#3f8fd4;
  --red:#e2383a;
  --ink:#333333;
  --white:#ffffff;
  --cream:#fffdf4;
}
*{box-sizing:border-box;margin:0;padding:0}
html,body{width:846px;height:1200px;overflow:hidden;background:#fff}
body{font-family:"M PLUS Rounded 1c",sans-serif;color:var(--ink)}
.flyer{position:relative;width:846px;height:1200px;overflow:hidden;background:var(--green-pale)}
.topbar{position:absolute;left:0;top:0;width:846px;height:62px;background:var(--white);display:flex;align-items:center;padding-left:14px;gap:22px;border-bottom:3px solid var(--green)}
.topbar__tag{background:var(--red);color:#fff;font-weight:900;font-size:24px;padding:4px 12px;border-radius:4px}
.topbar__lead{color:var(--green-dark);font-weight:900;font-size:29px;letter-spacing:1px;word-spacing:10px}
.hero{position:absolute;left:0;top:62px;width:846px;height:222px;background:linear-gradient(180deg,#f6fbef,#e1f0c9)}
.hero__tagline{position:absolute;left:400px;top:30px;background:#fff;border:3px solid var(--green);border-radius:10px;padding:4px 16px 6px;text-align:center;white-space:nowrap}
.hero__tagline small{display:block;font-size:17px;font-weight:800;color:var(--green-dark)}
.hero__tagline strong{display:block;font-size:30px;font-weight:900;color:var(--ink);line-height:1.1}
.hero__title{position:absolute;left:26px;top:46px;color:var(--green-dark);font-weight:900;font-size:80px;line-height:1;letter-spacing:2px;white-space:nowrap}
.hero__title span{display:block}
.hero__title span+span{margin-top:8px}
.hero__figure{position:absolute;left:660px;top:8px;width:160px;height:120px;border-radius:80px 80px 14px 14px;background:linear-gradient(180deg,#cfe6f7,#8fc0e8)}
.card{position:absolute;background:#fff;border-radius:12px;overflow:hidden;box-shadow:0 2px 0 rgba(0,0,0,.08)}
.card__head{height:46px;background:var(--blue);color:#fff;font-weight:900;font-size:26px;display:flex;align-items:center;padding-left:14px;gap:10px}
.card__head::before{content:"";width:18px;height:18px;border-radius:50%;background:#fff}
.card__body{position:relative;padding:12px 16px;font-weight:700;font-size:20px;line-height:1.45}
.card--side .card__head{background:var(--green);justify-content:center;padding-left:0}
.card--side .card__head::before{display:none}
.card--side .card__body{font-size:17px;line-height:1.5}
.list{list-style:none;font-size:27px;font-weight:900;line-height:1.6}
.list li::before{content:"●";color:var(--green);margin-right:6px}
.note{font-size:16px;font-weight:700;margin-top:6px}
.art{position:absolute;border-radius:10px}
.callout{position:absolute;left:28px;top:986px;width:488px;height:128px;background:var(--cream);border:4px solid var(--red);border-radius:12px}
.callout__kicker{position:absolute;left:130px;top:6px;font-size:16px;font-weight:800;color:var(--red);line-height:20px;white-space:nowrap}
.callout__main{position:absolute;left:130px;top:28px;font-size:28px;font-weight:900;color:var(--red);line-height:34px;white-space:nowrap}
.callout__text{position:absolute;left:130px;top:66px;font-size:13px;font-weight:700;line-height:18px;white-space:nowrap}
.callout__figure{position:absolute;left:14px;top:12px;width:104px;height:96px;border-radius:50px 50px 10px 10px;background:linear-gradient(180deg,#d2e8f6,#9ec8ea)}
.cards-ok{position:absolute;left:536px;top:976px;width:288px;height:134px;background:#fff;border:3px solid var(--green);border-radius:12px;padding:10px 10px}
.cards-ok__title{font-size:17px;font-weight:900;text-align:center;color:var(--ink);border-bottom:2px dashed var(--green);padding-bottom:8px;white-space:nowrap;line-height:26px}
.cards-ok__row{display:flex;gap:8px;margin-top:22px;justify-content:center}
.cards-ok__row span{width:44px;height:30px;border-radius:4px;background:#dfe6ee;border:1px solid #b8c3cf}
.footer{position:absolute;left:0;top:1120px;width:846px;height:80px;background:var(--green)}
.footer__name{position:absolute;left:0;top:0;width:300px;height:26px;background:var(--green-dark);color:#fff;font-size:17px;font-weight:800;padding-left:16px;line-height:26px}
.footer__phone{position:absolute;left:14px;top:28px;display:flex;align-items:center;gap:8px;color:#fff;font-weight:900;font-size:46px;line-height:50px;white-space:nowrap}
.footer__info{position:absolute;left:476px;top:5px;color:#fff;font-weight:800;font-size:14px;line-height:18px;white-space:nowrap}
.footer__hours{display:flex;align-items:center;gap:8px;margin-top:5px;font-size:21px;font-weight:900;line-height:24px}
.footer__hours em{font-style:normal;background:#fff;color:var(--green-dark);font-size:13px;line-height:18px;padding:0 6px;border-radius:3px}
.footer__hours + .footer__hours{margin-top:3px;font-size:16px;line-height:20px}
</style>
</head>
<body>
<div class="flyer">
  <header class="topbar">
    <span class="topbar__tag">完全保存版!</span>
    <span class="topbar__lead">必ずお役にたちます! お任せください!</span>
  </header>

  <section class="hero">
    <h1 class="hero__title"><span>そよかぜ</span><span>クリーンサービス</span></h1>
    <div class="hero__tagline"><small>暮らしの困った!に</small><strong>断捨離請負人</strong></div>
    <div class="hero__figure" role="img" aria-label="作業着の男性スタッフのイラスト"></div>
  </section>

  <article class="card" style="left:28px;top:296px;width:488px;height:226px">
    <h2 class="card__head">暮らしのお片付け</h2>
    <div class="card__body">
      <ul class="list"><li>ゴミ屋敷をピカピカに!</li><li>ベランダのお掃除!</li><li>不用品の処分!</li></ul>
      <div class="art" style="left:356px;top:18px;width:118px;height:140px;background:linear-gradient(180deg,#eef1f4,#c9d0d8)" role="img" aria-label="ゴミ袋と家具のイラスト"></div>
    </div>
  </article>

  <article class="card" style="left:28px;top:536px;width:488px;height:220px">
    <h2 class="card__head">遺品の整理</h2>
    <div class="card__body">
      <p style="width:310px">思い出が詰まった大切な遺品。<br>当社が丁寧に整理致します。</p>
      <p class="note" style="width:310px">その他、遺品に関するお悩み<br>ご相談承ります。</p>
      <div class="art" style="left:330px;top:16px;width:142px;height:132px;background:linear-gradient(180deg,#f1e9dc,#cdbca2)" role="img" aria-label="写真立てとカメラのイラスト"></div>
    </div>
  </article>

  <article class="card" style="left:28px;top:768px;width:488px;height:206px">
    <h2 class="card__head">トランクルームのお片付け</h2>
    <div class="card__body">
      <p style="width:290px">お荷物を指定の場所まで<br>お運びします!</p>
      <p class="note">もちろん、不用品処分承ります!</p>
      <div class="art" style="left:306px;top:14px;width:166px;height:122px;background:linear-gradient(180deg,#e3f0fa,#a9cfee)" role="img" aria-label="荷物を積んだトラックのイラスト"></div>
    </div>
  </article>

  <article class="card card--side" style="left:536px;top:296px;width:288px;height:234px">
    <h2 class="card__head">リフォーム</h2>
    <div class="card__body">
      <p style="width:150px">遺品整理後の壁紙張替から床の張替・エアコン取付なども!小さなことから大きなことまでご相談ください!</p>
      <div class="art" style="left:170px;top:26px;width:106px;height:120px;background:linear-gradient(180deg,#f3e4cc,#c99d67)" role="img" aria-label="床と壁を張り替えた部屋のイラスト"></div>
    </div>
  </article>

  <article class="card card--side" style="left:536px;top:542px;width:288px;height:204px">
    <h2 class="card__head">電気の困った</h2>
    <div class="card__body">
      <p>エアコンの取外しや<br>ウォシュレットの交換なども!<br>電気の困ったご相談下さい。</p>
      <div class="art" style="left:60px;top:96px;width:168px;height:42px;background:linear-gradient(180deg,#f7f8f9,#d3d8de)" role="img" aria-label="エアコンのイラスト"></div>
    </div>
  </article>

  <article class="card card--side" style="left:536px;top:758px;width:288px;height:208px">
    <h2 class="card__head">高価買取</h2>
    <div class="card__body">
      <p style="width:176px">ただ処分するだけではありません!まだ使える家具・貴金属等高価買取致します!ご相談下さい。</p>
      <div class="art" style="left:196px;top:50px;width:80px;height:80px;border-radius:50%;background:radial-gradient(circle,#fff7d6,#e2c56a)" role="img" aria-label="指輪のイラスト"></div>
    </div>
  </article>

  <aside class="cards-ok">
    <p class="cards-ok__title">各種クレジットカードOK!!</p>
    <div class="cards-ok__row"><span></span><span></span><span></span><span></span><span></span></div>
  </aside>

  <section class="callout">
    <div class="callout__figure" role="img" aria-label="電話を受けるスタッフのイラスト"></div>
    <p class="callout__kicker">お部屋をキレイに!毎日を快適に!</p>
    <p class="callout__main">まずはお電話でお見積を!</p>
    <p class="callout__text">よろしければまずはお電話ください。<br>どんなことでもお気軽にご相談ください。<br>お見積は無料です。</p>
  </section>

  <footer class="footer">
    <div class="footer__name">そよかぜクリーンサービス</div>
    <div class="footer__phone">
      <svg width="44" height="44" viewBox="0 0 24 24" aria-hidden="true"><circle cx="12" cy="12" r="11" fill="none" stroke="#fff" stroke-width="2"/><path d="M8.2 6.5c.5-.4 1.2-.3 1.5.2l1 1.7c.3.5.1 1.1-.3 1.4l-.7.5c.5 1.3 1.6 2.5 3 3.1l.5-.7c.3-.5.9-.6 1.4-.3l1.7 1c.5.3.6 1 .2 1.5l-.8.9c-.6.6-1.6.8-2.4.4-2.6-1.2-4.6-3.2-5.7-5.800-.4-.8-.2-1.8.4-2.4z" fill="#fff"/></svg>
      <span>0000-000-000</span>
    </div>
    <div class="footer__info">
      <p>東京都杉並区緑町2-14-5 (株)みどりリンク</p>
      <p class="footer__hours"><em>お電話受付</em>AM9:00〜PM8:00</p>
      <p class="footer__hours"><em>定休日</em>日曜日</p>
    </div>
  </footer>
</div>
</body>
</html>
```